Visual identity for an online reservation system company

We need a designer to re-create our visual identity. We are a startup based in São Paulo - Brazil specialized in Customer Management System for restaurants.
Project is composed of :
1. Visuals (no development needed, neither content) for our very basic portal. Some 4 images, menu and content position is up to our designer.
2. Visuals for two personalized modules for our customers (some sort of advanced calendar)
Everything is detailed in the briefing enclosed. Where there is a descriptive arrow, there is a needed image.
Target Market(s)
Our market is made of professionals (restaurant owners) who most of the time do not have an IT knowledge.
Industry/Entity Type
It Company
Look and feel
Each slider illustrates characteristics of the customer's brand and the style your logo design should communicate.

```html
<!DOCTYPE html>
<html lang="pt-BR">
<head>
<meta charset="utf-8">
<title>Mesa Cheia – Reservas</title>
<link href="https://fonts.googleapis.com/css2?family=Didact+Gothic&family=Nunito:wght@600;700;800&display=swap" rel="stylesheet">
<style>
:root{
  --ink:#1c1c1c;
  --header:#111;
  --paper:#e4ddd2;
  --floor:#f0eeef;
  --card:#fff;
  --wine:#7b1a3e;
  --wine-dark:#5a1130;
  --wine-deep:#46102a;
  --cell:#f1ece2;
  --muted:#cfc6b9;
  --label:#3a3a3a;
  --field:#f7f1ef;
  --field-line:#d9b9c4;
}
*{box-sizing:border-box;margin:0;padding:0}
html,body{width:906px;height:1200px;overflow:hidden}
body{position:relative;font-family:"Didact Gothic",sans-serif;color:var(--ink);
  background:linear-gradient(var(--paper) 0,#ece6dc 560px,#e7e0d5 670px,var(--floor) 670px)}
.abs{position:absolute}
/* header */
.site-header{left:0;top:0;width:906px;height:100px;background:linear-gradient(#2a2a2a,#0c0c0c);border-bottom:4px solid #3a3a3a}
.header-tab{left:370px;top:96px}
.brand{left:27px;top:22px;font-size:44px;color:#f2f2f2;letter-spacing:.5px}
.crowd{left:377px;top:30px;width:150px;height:47px;background:linear-gradient(#e8e8e8,#bdbdbd);border-radius:4px}
.nav a{position:absolute;color:#d8d8d8;font-size:16px;text-decoration:none;white-space:nowrap}
.nav .sep{position:absolute;width:1px;height:20px;background:#666}
/* slider card */
.slider-card{left:34px;top:157px;width:820px;height:406px;background:var(--card);box-shadow:0 8px 14px -6px rgba(0,0,0,.35)}
.photo{left:24px;top:28px;width:511px;height:311px;background:linear-gradient(160deg,#e9dcc4,#b58a55 45%,#6d4a2a 70%,#e8e2d8)}
.dots{left:224px;top:355px;display:flex;gap:22px}
.dots span{width:11px;height:11px;border-radius:50%;background:#e0cda8}
.dots span:first-child{background:#555}
.signin-title{left:570px;top:74px;font-size:21px;color:#555;width:250px;padding-bottom:6px;border-bottom:1px solid #ddd}
.social-login{left:598px;top:141px;width:157px;height:24px;background:linear-gradient(#4c68a6,#344f8a);color:#fff;font-size:12px;display:flex;align-items:center;gap:8px;padding-left:6px;font-family:"Nunito",sans-serif;font-weight:700}
.social-login i{width:14px;height:14px;background:#fff;display:block}
.field-label{font-size:11px;color:var(--label);font-family:"Nunito",sans-serif;font-weight:600}
.field{height:18px;background:var(--field);border:1px solid #e3cfc4;border-radius:3px}
.btn-sm{width:50px;height:24px;font-size:11px;color:#fff;display:flex;align-items:center;justify-content:center;font-family:"Nunito",sans-serif;font-weight:700}
/* calendar */
.calendar-card{left:63px;top:624px;width:424px;height:386px;background:var(--card);box-shadow:0 2px 6px rgba(0,0,0,.12)}
.calendar{left:19px;top:24px;width:427px;border:2px solid var(--wine);width:387px;background:var(--cell)}
.cal-head{height:52px;background:linear-gradient(#9a2a52,var(--wine-dark));color:#fff;display:flex;align-items:center;justify-content:center;font-family:"Nunito",sans-serif;font-weight:700;font-size:31px;position:relative}
.cal-head .arr{position:absolute;top:19px;width:0;height:0;border-top:8px solid transparent;border-bottom:8px solid transparent}
.cal-head .prev{left:10px;border-right:14px solid #e9c7d3}
.cal-head .next{right:10px;border-left:14px solid #e9c7d3}
.cal-grid{display:grid;grid-template-columns:repeat(7,1fr)}
.dow{height:30px;background:var(--wine-deep);color:#fff;display:flex;align-items:center;justify-content:center;font-family:"Nunito",sans-serif;font-weight:700;font-size:15px;border-right:1px solid #6a2040}
.day{height:42.3px;display:flex;align-items:center;justify-content:center;font-family:"Nunito",sans-serif;font-weight:800;font-size:25px;color:#222;border-right:1px solid #fff;border-bottom:1px solid #fff}
.day.out{color:var(--muted);font-weight:600}
.day.sel{background:var(--wine);color:#fff}
.day.sel-dark{background:var(--wine-deep);color:#fff}
.day.today{background:#c9c1b4}
/* time */
.panel{background:var(--card);box-shadow:0 2px 6px rgba(0,0,0,.12)}
.panel-band{background:var(--wine-dark);color:#fff;font-family:"Nunito",sans-serif;font-weight:700;font-size:17px;display:flex;align-items:center;justify-content:center;text-align:center}
.digit{width:44px;height:75px;background:linear-gradient(#86244a,var(--wine-deep));color:#fff;font-family:"Nunito",sans-serif;font-weight:600;font-size:58px;display:flex;align-items:center;justify-content:center;border-radius:2px}
.colon{font-size:44px;font-family:"Nunito",sans-serif;font-weight:800}
.tri{width:0;height:0;border-left:7px solid transparent;border-right:7px solid transparent}
.tri.up{border-bottom:11px solid var(--wine-deep)}
.tri.down{border-top:11px solid var(--wine-deep)}
.form-label{width:90px;text-align:right;font-size:11px;font-family:"Nunito",sans-serif;font-weight:700;color:#2a2a2a}
.form-field{width:164px;height:18px;border:1px solid var(--field-line);border-radius:3px;background:#fbf7f8}
.select{width:55px;height:18px;border:1px solid #cdb8c0;border-radius:3px;background:#f4eef0;font-size:11px;font-family:"Nunito",sans-serif;font-weight:700;padding-left:20px;line-height:16px}
.big-btn{width:119px;height:43px;background:linear-gradient(#8e2750,var(--wine-dark));color:#fff;font-family:"Nunito",sans-serif;font-weight:700;font-size:22px;display:flex;align-items:center;justify-content:center;border-radius:0 0 24px 24px;box-shadow:0 3px 4px rgba(0,0,0,.3)}
/* footer */
.footer-line{left:34px;top:1105px;width:836px;height:2px;background:#e2dfe0}
.footer-text{left:40px;font-size:11px;color:#777}
.social{width:31px;height:31px;border-radius:5px}
</style>
</head>
<body>
<header class="site-header abs">
  <div class="brand abs">Mesa Cheia</div>
  <div class="crowd abs" role="img" aria-label="Silhuetas de pessoas em grupo"></div>
  <nav class="nav">
    <a style="left:552px;top:29px">Quem Somos</a><span class="sep" style="left:664px;top:28px"></span>
    <a style="left:680px;top:29px">Demo</a><span class="sep" style="left:739px;top:28px"></span>
    <a style="left:754px;top:29px">Outros&nbsp; modulos</a>
    <a style="left:552px;top:60px">Espaço cliente</a><span class="sep" style="left:677px;top:59px"></span>
    <a style="left:697px;top:60px">Contato</a>
  </nav>
</header>
<svg class="header-tab abs" width="166" height="30" viewBox="0 0 166 30"><path d="M0 0 Q40 0 60 18 Q83 32 106 18 Q126 0 166 0 Z" fill="#111"/></svg>

<section class="slider-card abs">
  <div class="photo abs" role="img" aria-label="Salão de restaurante com mesa posta e taças"></div>
  <div class="dots abs"><span></span><span></span><span></span><span></span></div>
  <h2 class="signin-title abs" style="font-weight:400">Sign in</h2>
  <div class="social-login abs"><i></i>Entre com Conecta</div>
  <span class="field-label abs" style="left:573px;top:208px">email:</span>
  <div class="field abs" style="left:626px;top:206px;width:164px"></div>
  <span class="field-label abs" style="left:573px;top:236px">Senha:</span>
  <div class="field abs" style="left:626px;top:234px;width:164px"></div>
  <div class="btn-sm abs" style="left:686px;top:264px;background:#7a6f66">Clear</div>
  <div class="btn-sm abs" style="left:741px;top:264px;background:#e9d6bd">OK</div>
</section>

<section class="calendar-card abs">
  <div class="calendar abs">
    <div class="cal-head"><span class="arr prev"></span>Janeiro 2013<span class="arr next"></span></div>
    <div class="cal-grid">
      <div class="dow">D</div><div class="dow">S</div><div class="dow">T</div><div class="dow">Q</div><div class="dow">Q</div><div class="dow">S</div><div class="dow">S</div>
      <div class="day out">30</div><div class="day out">31</div><div class="day">1</div><div class="day">2</div><div class="day">3</div><div class="day">4</div><div class="day">5</div>
      <div class="day">6</div><div class="day">7</div><div class="day">8</div><div class="day">9</div><div class="day">10</div><div class="day sel">11</div><div class="day">12</div>
      <div class="day">13</div><div class="day">14</div><div class="day sel">15</div><div class="day">16</div><div class="day">17</div><div class="day">18</div><div class="day">19</div>
      <div class="day">20</div><div class="day">21</div><div class="day">22</div><div class="day">23</div><div class="day">24</div><div class="day sel-dark">25</div><div class="day">26</div>
      <div class="day">27</div><div class="day today">28</div><div class="day">29</div><div class="day sel">30</div><div class="day">31</div><div class="day out">1</div><div class="day out">2</div>
      <div class="day out">2</div><div class="day out">3</div><div class="day out">4</div><div class="day out">5</div><div class="day out">6</div><div class="day out">7</div><div class="day out">8</div>
    </div>
  </div>
</section>

<section class="panel abs" style="left:513px;top:625px;width:325px;height:151px">
  <div class="panel-band" style="height:46px">Indique a hora da sua reserva</div>
  <div class="tri up abs" style="left:26px;top:71px"></div>
  <div class="tri down abs" style="left:26px;top:110px"></div>
  <div class="digit abs" style="left:54px;top:59px">2</div>
  <div class="digit abs" style="left:105px;top:59px">0</div>
  <div class="colon abs" style="left:163px;top:66px">:</div>
  <div class="digit abs" style="left:174px;top:59px">0</div>
  <div class="digit abs" style="left:224px;top:59px">0</div>
  <div class="tri up abs" style="left:290px;top:71px"></div>
  <div class="tri down abs" style="left:290px;top:110px"></div>
</section>

<section class="panel abs" style="left:513px;top:795px;width:325px;height:215px">
  <div class="panel-band" style="height:65px;padding:0 40px">Reserve para o 25 janeiro as 12:00!</div>
  <span class="form-label abs" style="left:0;top:82px;width:136px">Numero de pessoas:</span>
  <div class="select abs" style="left:167px;top:80px">5
    <svg class="abs" style="right:4px;top:4px" width="12" height="8"><path d="M1 1 L6 7 L11 1" fill="none" stroke="#b79aa6" stroke-width="1.5"/></svg></div>
  <span class="form-label abs" style="left:2px;top:107px">Nome:</span>
  <div class="form-field abs" style="left:115px;top:105px"></div>
  <span class="form-label abs" style="left:2px;top:132px">Sobrenome:</span>
  <div class="form-field abs" style="left:115px;top:130px"></div>
  <span class="form-label abs" style="left:2px;top:157px">Telefone:</span>
  <div class="form-field abs" style="left:115px;top:155px"></div>
  <span class="form-label abs" style="left:2px;top:182px">email:</span>
  <div class="form-field abs" style="left:115px;top:180px"></div>
</section>
<div class="big-btn abs" style="left:539px;top:1010px">Voltar</div>
<div class="big-btn abs" style="left:686px;top:1010px">OK</div>

<footer>
  <div class="footer-line abs"></div>
  <p class="footer-text abs" style="top:1136px">Copyright Mesa Cheia 2012 – 2013</p>
  <p class="footer-text abs" style="top:1157px">Contate-nos: contato@mesacheia.com.br</p>
  <div class="social abs" style="left:790px;top:1137px;background:#8a8aa6" role="img" aria-label="Rede social"></div>
  <div class="social abs" style="left:836px;top:1137px;background:#7fb0c4" role="img" aria-label="Rede social"></div>
</footer>
</body>
</html>
```